BrightOak Lending Needs a Stated Income Flyer

We need a flyer created for our Stated Income loan program, using the color scheme to match our company logo.
I've included a stock photo to be used and within that photo, we want Funded stamped in red on the blank poster board.
For the written part of the flyer, we want the word State Income in red.
On the bottom part (Contact Us), we want to make it possible for us to edit for any future loan officer we hire along the way to include their contact information.
We like the flyer for VeroCredit.
Industry/Entity Type
Loan

```html
<!DOCTYPE html>
<html lang="en">
<head>
<meta charset="utf-8">
<title>BrightOak Lending – Stated Income Flyer</title>
<link rel="stylesheet" href="https://fonts.googleapis.com/css2?family=Alfa+Slab+One&family=Carlito:wght@400;700&family=Open+Sans:wght@400;700&family=Questrial&family=Roboto+Condensed:wght@700&display=swap">
<style>
:root{
  --navy:#1a4a8e;
  --navy-deep:#123a73;
  --red:#9b1c22;
  --ink:#2b2b2b;
  --white:#ffffff;
}
*{margin:0;padding:0;box-sizing:border-box}
html,body{width:927px;height:1200px;overflow:hidden;background:var(--white)}
.flyer{position:relative;width:927px;height:1200px;overflow:hidden;background:var(--white);font-family:"Questrial",sans-serif;color:var(--ink)}
.brand{position:absolute;left:15px;top:14px;width:320px;height:90px;display:flex;align-items:center;gap:12px;padding-left:12px;white-space:nowrap}
.brand-mark{flex:none;width:40px;height:40px;background:var(--navy)}
.brand-name{font-family:"Open Sans",sans-serif;font-weight:700;font-size:29px;color:var(--navy);letter-spacing:-.5px}
.top-rule{position:absolute;left:0;top:114px;width:927px;height:14px;background:linear-gradient(180deg,var(--navy-deep) 0 55%,#9aa9c2 55% 100%)}
.photo{position:absolute;left:0;top:130px;width:540px;height:620px;background:linear-gradient(120deg,#d9c2b0 0%,#b9a596 35%,#9a9694 60%,#ecebe9 100%)}
.stamp{position:absolute;left:30px;top:478px;font-family:"Alfa Slab One",serif;font-size:78px;color:var(--red);letter-spacing:2px;transform:rotate(-11deg);transform-origin:left top}
.stated{position:absolute;right:29px;top:145px;font-family:"Roboto Condensed",sans-serif;font-weight:700;font-size:56px;line-height:1;color:var(--red);white-space:nowrap}
.fast{position:absolute;right:29px;top:200px;font-size:42px;line-height:1;letter-spacing:1px;color:var(--navy);white-space:nowrap}
.program{position:absolute;right:28px;top:262px;text-align:right;font-size:26px;line-height:32px;color:var(--ink)}
.property-types{position:absolute;right:28px;top:342px;text-align:right;font-size:17px;line-height:24px;color:#3a3a3a;white-space:nowrap}
.perks{position:absolute;left:540px;top:405px;width:370px;list-style:none;font-size:19.5px;line-height:24px;color:#333}
.perks li{position:relative;padding-left:21px;margin-bottom:14.5px}
.perks li::before{content:"";position:absolute;left:0;top:10px;width:6px;height:6px;border-radius:50%;background:#333}
.band{position:absolute;left:0;top:690px;width:927px;height:356px}
.rates{position:absolute;left:0;top:810px;width:500px;text-align:center;color:var(--white);font-family:"Open Sans",sans-serif;font-weight:700}
.rates .lead{font-size:34px;line-height:44px;white-space:nowrap}
.rates .term{font-size:24px;line-height:32px;margin-top:14px}
.terms{position:absolute;left:537px;top:785px;width:335px;list-style:none;color:var(--white);font-family:"Open Sans",sans-serif;font-weight:700;font-size:20px;line-height:24px}
.terms li{position:relative;padding-left:26px;margin-bottom:14px}
.terms li::before{content:"";position:absolute;left:0;top:5px;width:11px;height:11px;background:var(--white)}
.contact{position:absolute;left:533px;top:1062px;font-family:"Carlito",sans-serif;font-style:normal;font-size:19px;line-height:25.5px;color:var(--ink)}
</style>
</head>
<body>
<div class="flyer">
  <header class="brand">
    <span class="brand-mark"></span>
    <span class="brand-name">BrightOak Lending</span>
  </header>
  <div class="top-rule"></div>

  <div class="photo" role="img" aria-label="Stock photo of cheering business people holding a poster board stamped FUNDED"></div>
  <div class="stamp">FUNDED</div>

  <h1 class="stated">STATED INCOME</h1>
  <p class="fast">FAST &amp; EASY</p>
  <p class="program">PURCHASE and<br>CASH OUT REFINANCE</p>
  <p class="property-types">Non-owner SFR/Condo/2-4 Units<br>5+ Units &amp; Commercial – Ask for Details</p>

  <ul class="perks">
    <li>No Tax Returns</li>
    <li>No 4506-T</li>
    <li>No Cash-Out Restrictions</li>
    <li>No Cash Reserves Required</li>
    <li>No Limit on Number of Properties owned or financed</li>
    <li>No DTI Calculation</li>
    <li>No Seasoned Funds – No Asset Disclosures (Purchase)</li>
  </ul>

  <svg class="band" viewBox="0 0 927 356" aria-hidden="true">
    <defs>
      <linearGradient id="swoosh" x1="0" x2="1" y1="0" y2="0">
        <stop offset="0" stop-color="#ffffff"/>
        <stop offset=".55" stop-color="#b7b7b7"/>
        <stop offset="1" stop-color="#6f6f6f"/>
      </linearGradient>
    </defs>
    <path d="M0 52 Q420 72 927 12 L927 34 Q430 84 0 64 Z" fill="url(#swoosh)"/>
    <path d="M0 60 Q430 80 927 26 L927 356 L0 356 Z" fill="#1a4a8e"/>
  </svg>

  <div class="rates">
    <p class="lead">RATES AS LOW AS 6.49%</p>
    <p class="term">3 &amp; 5 Year Fixed ARM – 30 Year<br>Amortization</p>
  </div>

  <ul class="terms">
    <li>Max Rebate 2%</li>
    <li>Max 70% Loan-to-value</li>
    <li>650 Min Credit Score</li>
    <li>Loan Amounts $100,000 to $2,000,000</li>
    <li>Lending to Corporations, LLC, Partnership &amp; Individuals</li>
  </ul>

  <address class="contact">
    Marcus Delano<br>
    888-555-0142<br>
    marcus@brightoaklending.com<br>
    BRE #02458913
  </address>
</div>
</body>
</html>
```